Business Card Design

I am a Building Surveyor and run my own Building Consultat company, providing professional advice and services to builders, architects, designers, owners, etc.

Industry/Entity Type

Business

Contact Information for Business Card

Dorwen Fasque BBldgSurv (Hons)
Managing Director

47 Marlow Crest, Kelvoth Downs WA 6158
Mobile 0498 153 607
Email Dorwen.fasque@ridgeplumbav.com

Requirements
Must have
• I would like the back of the business card to be one colour (a shade of either black or maroon, matching the colours of my logo). Positioned in the centre on the back of the business card is to be my logo.

The front of the card is to be white, with my contact information in either black or maroon. The ADBldgSurv after my name should be in a smaller font size than my name. I would also like a small logo somewhere on this side of the card.

```html
<!DOCTYPE html>
<html lang="en">
<head>
<meta charset="utf-8">
<title>Ridgeplumb Building Advisory – Business Card</title>
<link rel="stylesheet" href="https://fonts.googleapis.com/css2?family=Open+Sans:wght@400;600;700&display=swap">
<style>
  :root {
    --stage: #2a2a2a;
    --maroon: #8e0f0c;
    --maroon-dark: #6e0806;
    --maroon-light: #a3201a;
    --white: #ffffff;
    --ink: #2b2b2b;
    --rule: #555555;
    --silver: #e6e6e6;
  }
  * { box-sizing: border-box; margin: 0; padding: 0; }
  html, body {
    width: 1200px; height: 1000px; overflow: hidden;
    background: var(--stage);
    font-family: "Open Sans", Arial, sans-serif;
  }
  .stage {
    position: relative; width: 1200px; height: 1000px;
  }
  .card {
    position: absolute; top: 345px;
    width: 500px; height: 306px;
    box-shadow: 0 10px 30px rgba(0,0,0,.5);
    overflow: hidden;
  }
  /* Back of card */
  .card-back {
    left: 70px;
    background: linear-gradient(180deg, var(--maroon-light) 0%, var(--maroon) 55%, var(--maroon-dark) 100%);
    display: flex; align-items: center; justify-content: center;
  }
  .brand { display: flex; flex-direction: column; align-items: center; color: var(--silver); }
  .brand-mark {
    width: 70px; height: 70px; border-radius: 50%;
    border: 4px solid var(--silver); margin-bottom: 10px;
  }
  .brand-name {
    font-weight: 600; font-size: 34px; letter-spacing: 2px; line-height: 1;
  }
  .brand-tag {
    display: flex; align-items: center; gap: 8px;
    font-weight: 600; font-size: 11px; letter-spacing: 2px; margin-top: 6px;
  }
  .brand-tag::before, .brand-tag::after {
    content: ""; width: 50px; height: 1px; background: currentColor; opacity: .7;
  }
  /* Front of card */
  .card-front { left: 630px; background: var(--white); }
  .front-brand {
    position: absolute; left: 22px; top: 34px;
    display: flex; align-items: center; gap: 10px; color: var(--ink);
  }
  .front-brand .brand-mark {
    width: 46px; height: 46px; border: 3px solid var(--maroon); margin: 0;
  }
  .front-brand .brand-name { font-size: 21px; letter-spacing: 1.5px; }
  .front-brand .brand-tag { font-size: 7px; margin-top: 3px; }
  .front-brand .brand-tag::before, .front-brand .brand-tag::after { width: 26px; }
  .front-brand .brand-words { display: flex; flex-direction: column; align-items: center; }
  .rule-top {
    position: absolute; left: 230px; right: 0; top: 62px; height: 1px; background: var(--rule);
  }
  .person { position: absolute; left: 270px; top: 68px; }
  .person-name {
    color: var(--maroon); font-weight: 700; font-size: 13px; text-transform: uppercase;
  }
  .person-name small { font-size: 8px; font-weight: 600; text-transform: none; margin-left: 3px; }
  .person-title { color: var(--ink); font-weight: 700; font-size: 10px; margin-top: 1px; }
  .rule-mid {
    position: absolute; left: 30px; right: 0; top: 128px; height: 1px; background: var(--rule);
  }
  .contact {
    position: absolute; left: 30px; top: 178px;
    display: grid; grid-template-columns: auto auto; column-gap: 6px; row-gap: 3px;
    font-size: 11px;
  }
  .contact dt { color: var(--maroon); font-weight: 700; text-align: right; }
  .contact dd { color: var(--ink); }
  .band {
    position: absolute; left: 0; right: 0; bottom: 0; height: 28px;
    background: var(--maroon);
    border-top: 5px solid var(--white);
    box-shadow: 0 -3px 0 var(--maroon-light);
  }
</style>
</head>
<body>
<main class="stage">
  <section class="card card-back" aria-label="Business card back">
    <div class="brand">
      <div class="brand-mark"></div>
      <div class="brand-name">RIDGEPLUMB</div>
      <div class="brand-tag">BUILDING ADVISORY</div>
    </div>
  </section>

  <section class="card card-front" aria-label="Business card front">
    <div class="front-brand brand">
      <div class="brand-mark"></div>
      <div class="brand-words">
        <div class="brand-name">RIDGEPLUMB</div>
        <div class="brand-tag">BUILDING ADVISORY</div>
      </div>
    </div>
    <div class="rule-top"></div>
    <div class="person">
      <p class="person-name">Dorwen Fasque<small>ADBldgSurv</small></p>
      <p class="person-title">DIRECTOR</p>
    </div>
    <div class="rule-mid"></div>
    <dl class="contact">
      <dt>Mobile:</dt><dd>0498 153 607</dd>
      <dt>Email:</dt><dd>Dorwen.fasque@ridgeplumbav.com</dd>
      <dt>Address:</dt><dd>47 Marlow Crest, Kelvoth Downs WA 6158</dd>
    </dl>
    <div class="band"></div>
  </section>
</main>
</body>
</html>
```